Restaurant menu design

Design fine dinning menu for Indian restaurant. Restaurant location is on river side. So if design has some touch of Yarra river of Melbourne and Indian touch. It is not compulsory. Creative and modern design is required.
I want to print in A3 and folded take away sizes so design should for both.
1. In A3, backside we need to design drink menu. I am attaching our current restaurant menu for drinks name and price.

Target Market(s)

Indian / Australian Customer

Industry/Entity Type

Indian Food, Indian fine dining

Colors
F0912C
F2A743
F7CA91
FBE8D2
FDF5EE

Requirements
Must have
• Simple but district design
Should not have
• common other restaurant type menu. Too many colours.

```html
<!DOCTYPE html>
<html lang="en">
<head>
<meta charset="utf-8">
<title>Tara's Kitchen Menu</title>
<link href="https://fonts.googleapis.com/css2?family=Poppins:wght@500;600;700&family=Roboto:wght@300;400&display=swap" rel="stylesheet">
<style>
:root{
  --backdrop:#585c5f;
  --paper:#ffffff;
  --ink:#0b0b0b;
  --muted:#555555;
  --rule:#333333;
}
*{margin:0;padding:0;box-sizing:border-box}
html,body{width:1200px;height:1200px;overflow:hidden;background:var(--backdrop)}
.menu-sheet{position:absolute;left:68px;top:221px;width:1059px;height:756px;background:var(--paper);box-shadow:0 2px 6px rgba(0,0,0,.35)}
.header-band{position:absolute;left:0;top:0;width:1059px;height:45px}
.menu-title{position:absolute;left:35px;top:10px;font:700 21px/1 'Poppins',sans-serif;color:#fff;letter-spacing:.2px}
.divider{position:absolute;top:60px;height:670px;border-left:1px solid var(--rule)}
.menu-section{position:absolute;font-family:'Poppins',sans-serif;color:var(--ink)}
.section-banner{display:inline-block;background:var(--ink);color:#fff;font:700 14.5px/22px 'Poppins',sans-serif;padding:0 17px 0 5px;height:22px;margin-bottom:10px;clip-path:polygon(0 0,100% 0,calc(100% - 7px) 50%,100% 100%,0 100%)}
.dish{margin-bottom:7px}
.dish-line{display:flex;align-items:baseline;font-size:9.2px;font-weight:600;line-height:11px}
.dish-line .leader{flex:1;border-bottom:1.2px dotted var(--ink);margin:0 3px;transform:translateY(-2px)}
.dish-line .price{font-weight:700;font-size:10px}
.dish-desc{font:300 7.1px/9px 'Roboto',sans-serif;color:var(--muted);margin-top:1px}
.col-two .dish-desc{max-width:205px}
.col-four .dish-desc{max-width:198px}
.plain-list .dish{margin-bottom:8px}
.plain-list .section-banner{margin-bottom:12px}
.bread-list .dish{margin-bottom:10px}
.brand-block{position:absolute;left:812px;top:668px;width:215px;text-align:center}
.brand-rule{height:4px;border-top:1px solid var(--ink);border-bottom:1px solid var(--ink)}
.brand-name{margin-top:24px;font:600 22px/1 'Poppins',sans-serif;color:var(--ink)}
</style>
</head>
<body>
<div class="menu-sheet">
  <svg class="header-band" viewBox="0 0 1059 45" aria-hidden="true">
    <path d="M0 0H1059V12H300C288 12 282 16 275 24L264 37C258 43 252 45 242 45H0Z" fill="#0b0b0b"/>
  </svg>
  <div class="menu-title">Tara’s Kitchen Menu</div>

  <div class="divider" style="left:278px"></div>
  <div class="divider" style="left:540px"></div>
  <div class="divider" style="left:793px"></div>

  <!-- Column 1 -->
  <section class="menu-section" style="left:35px;top:63px;width:225px">
    <h2 class="section-banner">Vegetarian Entrées</h2>
    <div class="dish"><div class="dish-line"><span>Classic Samosa</span><span class="leader"></span><span class="price">$16</span></div><p class="dish-desc">Handcrafted pastry parcels filled with spiced potatoes &amp; peas, served with a duo of fresh mint-coriander chutney and sweet mango relish.</p></div>
    <div class="dish"><div class="dish-line"><span>Crispy Onion &amp; Spinach Bhaji</span><span class="leader"></span><span class="price">$16</span></div><p class="dish-desc">Crisp golden fritters of baby spinach &amp; onion, delicately spiced, paired with house chutneys.</p></div>
    <div class="dish"><div class="dish-line"><span>Harabhara Edamame Kebab</span><span class="leader" style="border:0"></span><span class="price">$18</span></div><p class="dish-desc">Pan-seared medallions of edamame and garden vegetables, stuffed with soft cheese and herbs, served with tangy yogurt dip.</p></div>
    <div class="dish"><div class="dish-line"><span>Zafrani Paneer Tikka</span><span class="leader"></span><span class="price">$22</span></div><p class="dish-desc">Cubes of cottage cheese marinated in saffron, cardamom &amp; smoky tandoor spices, grilled to perfection, served with mint chutney and microgreens.</p></div>
    <div class="dish"><div class="dish-line"><span>Vada Pav Sliders</span><span class="leader"></span><span class="price">$16</span></div><p class="dish-desc">A gourmet take on Mumbai’s street legend: spiced potato croquette in a butter brioche bun, layered with tamarind, mint-coriander chutney &amp; fiery thecha, accompanied by crisp fried green chilli.</p></div>
  </section>
  <section class="menu-section" style="left:35px;top:314px;width:225px">
    <h2 class="section-banner">Non-Vegetarian Entrées</h2>
    <div class="dish"><div class="dish-line"><span>Smoke Tandoori Chicken Tikka</span><span class="leader"></span><span class="price">$20</span></div><p class="dish-desc">Charcoal-grilled chicken marinated overnight with aromatic spices, finished with a touch of smokey infusion.</p></div>
    <div class="dish"><div class="dish-line"><span>Chicken Malai Tikka</span><span class="leader"></span><span class="price">$20</span></div><p class="dish-desc">Tender chicken morsels marinated in cream, cheese &amp; cardamom, cooked gently in the tandoor for a melt-in-mouth experience.</p></div>
    <div class="dish"><div class="dish-line"><span>Awadhi Fish Tikka</span><span class="leader"></span><span class="price">$22</span></div><p class="dish-desc">Fresh barramundi fillets marinated with hand-pounded Awadhi spices, grilled for a delicate smokey finish.</p></div>
    <div class="dish"><div class="dish-line"><span>Tandoori Tiger Prawns</span><span class="leader"></span><span class="price">$24</span></div><p class="dish-desc">Jumbo prawns infused with curry-leaf butter, garlic &amp; chilli, char-grilled for an indulgent coastal flavour.</p></div>
    <div class="dish"><div class="dish-line"><span>Lamb Gilafi Seekh</span><span class="leader"></span><span class="price">$22</span></div><p class="dish-desc">Minced lamb spiced with herbs, peppers &amp; aromatics, skewered &amp; flame-roasted, served with minted yogurt.</p></div>
    <div class="dish"><div class="dish-line"><span>Tandoori Platter</span><span class="leader"></span><span class="price">$39</span></div><p class="dish-desc">A chef’s selection of smoky tandoori classics: Chicken Tikka, Malai Tikka, Lamb Seekh &amp; Awadhi Fish, presented with a medley of chutneys &amp; dips.</p></div>
  </section>
  <section class="menu-section" style="left:35px;top:596px;width:225px">
    <h2 class="section-banner" style="margin-bottom:6px">Chaat</h2>
    <div class="dish"><div class="dish-line"><span>Panipuri Experience</span><span class="leader"></span><span class="price">$20</span></div><p class="dish-desc">Crisp puris filled with spiced potato, tangy chutneys &amp; chilled spiced water — a refined version of the street favourite.</p></div>
    <div class="dish"><div class="dish-line"><span>Burrata Chaat</span><span class="leader"></span><span class="price">$20</span></div><p class="dish-desc">Creamy burrata resting on crispy papdi, layered with tamarind glaze, mint chutney &amp; golden sev.</p></div>
    <div class="dish"><div class="dish-line"><span>Deconstructed Samosa Chaat</span><span class="leader"></span><span class="price">$18</span></div><p class="dish-desc">Crispy samosa pastry crumbles over spiced potato &amp; peas, dressed with chutneys, yogurt &amp; pomegranate jewels.</p></div>
  </section>

  <!-- Column 2 -->
  <section class="menu-section col-two" style="left:294px;top:63px;width:227px">
    <h2 class="section-banner">Indo-Chinese</h2>
    <div class="dish"><div class="dish-line"><span>Vegetable Manchurian Dry</span><span class="leader"></span><span class="price">$22</span></div><p class="dish-desc">Golden-fried vegetable dumplings wok-tossed in garlic, chilli &amp; soy glaze.</p></div>
    <div class="dish"><div class="dish-line"><span>Paneer Chilli Dry</span><span class="leader"></span><span class="price">$24</span></div><p class="dish-desc">Cottage cheese cubes tossed with peppers, onions &amp; chilli-garlic soy reduction.</p></div>
    <div class="dish"><div class="dish-line"><span>Chilli Chicken Dry</span><span class="leader"></span><span class="price">$26</span></div><p class="dish-desc">Tender chicken tossed with shallots, peppers &amp; fiery Indo-Chinese sauce.</p></div>
    <div class="dish"><div class="dish-line"><span>Oriental Noodles</span><span class="leader" style="flex:0 0 26px"></span><span class="price">Veg $22 / Chicken $24</span></div><p class="dish-desc">Stir-fried noodles with seasonal vegetables, wok-seared with soy &amp; garlic.</p></div>
  </section>
  <section class="menu-section col-two plain-list" style="left:294px;top:256px;width:227px">
    <h2 class="section-banner">Classic Curries</h2>
    <div class="dish"><div class="dish-line"><span>Paneer / Kofta / Mixed Veg</span><span class="leader"></span><span class="price">$26</span></div><p class="dish-desc">Choose your protein with a choice of gourmet curry bases.</p></div>
    <div class="dish"><div class="dish-line"><span>Chicken / Lamb</span><span class="leader"></span><span class="price">$28</span></div><p class="dish-desc">Choose your protein with a choice of gourmet curry bases.</p></div>
    <div class="dish"><div class="dish-line"><span>Prawns / Fish</span><span class="leader"></span><span class="price">$30</span></div><p class="dish-desc">Choose your protein with a choice of gourmet curry bases.</p></div>
    <div class="dish"><div class="dish-line"><span>Vindaloo</span></div><p class="dish-desc">Fiery Goan-style curry with red chillies &amp; vinegar.</p></div>
    <div class="dish"><div class="dish-line"><span>Saag</span></div><p class="dish-desc">Creamy buttered spinach slow-cooked with spices.</p></div>
    <div class="dish"><div class="dish-line"><span>Korma</span></div><p class="dish-desc">Mild, creamy cashew &amp; saffron curry.</p></div>
    <div class="dish"><div class="dish-line"><span>Masala</span></div><p class="dish-desc">Tomato &amp; onion base enriched with cream &amp; butter.</p></div>
    <div class="dish"><div class="dish-line"><span>Madras</span></div><p class="dish-desc">Coconut-based curry with onions, garlic &amp; curry leaves.</p></div>
  </section>
  <section class="menu-section col-two" style="left:294px;top:530px;width:227px">
    <h2 class="section-banner">Non-Vegetarian Mains</h2>
    <div class="dish" style="margin-bottom:4px"><div class="dish-line"><span>Raja Rani Chicken</span><span class="leader"></span><span class="price">$35</span></div><p class="dish-desc">Char-grilled chicken tikka wrapped in a silky egg roll, layered with makhani sauce &amp; spinach gravy — regal flavours in every bite.</p></div>
    <div class="dish"><div class="dish-line"><span>Butter Chicken</span><span class="leader"></span><span class="price">$29</span></div><p class="dish-desc">A refined Delhi classic: chicken simmered in a tomato-butter sauce, smoky &amp; velvety.</p></div>
    <div class="dish"><div class="dish-line"><span>Lamb Rogan Josh</span><span class="leader"></span><span class="price">$29</span></div><p class="dish-desc">Kashmiri-style lamb curry, slow-braised in aromatic spices with a deep, rich flavour.</p></div>
    <div class="dish"><div class="dish-line"><span>Dhaba Goat Masala</span><span class="leader"></span><span class="price">$29</span></div><p class="dish-desc">A rustic North Indian goat curry, slow-cooked with onions, garlic, and earthy spices — inspired by India’s iconic roadside kitchens.</p></div>
  </section>

  <!-- Column 3 -->
  <section class="menu-section" style="left:558px;top:63px;width:218px">
    <h2 class="section-banner">Vegetarian Entrées</h2>
    <div class="dish"><div class="dish-line"><span>Sham Savera Kofta</span><span class="leader"></span><span class="price">$26</span></div><p class="dish-desc">Spinach dumplings filled with cottage cheese, simmered in a rich tomato-butter sauce — a true royal delicacy.</p></div>
    <div class="dish"><div class="dish-line"><span>Mexican Salsa Paneer</span><span class="leader"></span><span class="price">$28</span></div><p class="dish-desc">Paneer cubes tossed in a fusion of roasted Mexican-style tomato salsa and Indian spices — a bold East-meets-West creation.</p></div>
    <div class="dish"><div class="dish-line"><span>Mushroom Mutter Masala</span><span class="leader"></span><span class="price">$28</span></div><p class="dish-desc">Tender mushrooms and garden peas in a spiced onion-tomato gravy, finished with cream.</p></div>
    <div class="dish"><div class="dish-line"><span>Kaju Curry</span><span class="leader"></span><span class="price">$28</span></div><p class="dish-desc">A luxurious cashew-based curry enriched with aromatic spices, velvety texture &amp; buttery finish.</p></div>
    <div class="dish"><div class="dish-line"><span>Cheese Butter Masala</span><span class="leader"></span><span class="price">$28</span></div><p class="dish-desc">Paneer and soft cheese in a creamy, butter-rich tomato gravy — indulgent &amp; comforting.</p></div>
    <div class="dish"><div class="dish-line"><span>Dal Tadka</span><span class="leader"></span><span class="price">$22</span></div><p class="dish-desc">Yellow lentils tempered with garlic, cumin &amp; chilli, offering homestyle comfort with gourmet finesse.</p></div>
    <div class="dish"><div class="dish-line"><span>Dal Makhani</span><span class="leader"></span><span class="price">$22</span></div><p class="dish-desc">Black lentils, slow-cooked overnight with butter and cream — a timeless Delhi specialty.</p></div>
    <div class="dish"><div class="dish-line"><span>Vegetable Dum Biryani</span><span class="leader"></span><span class="price">$28</span></div><p class="dish-desc" style="max-width:205px">Saffron-scented basmati rice layered with seasonal vegetables, sealed and slow-cooked in the dum style, served with cooling raita.</p></div>
  </section>
  <section class="menu-section" style="left:558px;top:418px;width:218px">
    <h2 class="section-banner">Rice &amp; Biryanis</h2>
    <div class="dish"><div class="dish-line"><span>Plain Basmati Rice</span><span class="leader"></span><span class="price">$8</span></div><p class="dish-desc">Steamed long-grain basmati rice, light &amp; fluffy.</p></div>
    <div class="dish"><div class="dish-line"><span>Jeera Rice</span><span class="leader"></span><span class="price">$8</span></div><p class="dish-desc">Basmati rice tempered with roasted cumin seeds.</p></div>
    <div class="dish"><div class="dish-line"><span>Lemon Coconut Rice</span><span class="leader"></span><span class="price">$10</span></div><p class="dish-desc">Fragrant rice infused with lemon zest, curry leaves &amp; coconut.</p></div>
    <div class="dish"><div class="dish-line"><span>Peas Pulao</span><span class="leader"></span><span class="price">$10</span></div><p class="dish-desc">Delicate basmati rice cooked with sweet garden peas &amp; whole spices.</p></div>
    <div class="dish"><div class="dish-line"><span>Biryani Flavoured Rice</span><span class="leader"></span><span class="price">$15</span></div><p class="dish-desc">Aromatic saffron basmati rice prepared in biryani style.</p></div>
    <div class="dish"><div class="dish-line"><span>Vegetable Dum Biryani</span><span class="leader"></span><span class="price">$28</span></div><p class="dish-desc">Classic layered vegetable biryani with saffron, slow-cooked dum style.</p></div>
    <div class="dish"><div class="dish-line"><span>Hyderabadi Chicken Biryani</span><span class="leader"></span><span class="price">$30</span></div><p class="dish-desc">Fragrant rice layered with marinated chicken, spices &amp; saffron, served with raita.</p></div>
    <div class="dish"><div class="dish-line"><span>Lamb Dum Biryani</span><span class="leader"></span><span class="price">$33</span></div><p class="dish-desc">A celebratory lamb shank biryani, slow-cooked with caramelised onions, saffron &amp; spices — rich and aromatic.</p></div>
  </section>

  <!-- Column 4 -->
  <section class="menu-section col-four bread-list" style="left:812px;top:63px;width:215px">
    <h2 class="section-banner">Breads</h2>
    <div class="dish"><div class="dish-line"><span>Classic Butter Naan</span><span class="leader"></span><span class="price">$6</span></div><p class="dish-desc">Soft, fluffy tandoor-baked bread brushed with butter.</p></div>
    <div class="dish"><div class="dish-line"><span>Garlic Naan</span><span class="leader"></span><span class="price">$7</span></div><p class="dish-desc">Tandoor-baked naan with fresh garlic &amp; coriander.</p></div>
    <div class="dish"><div class="dish-line"><span>Lachha Paratha</span><span class="leader"></span><span class="price">$8</span></div><p class="dish-desc">Crisp, flaky, multi-layered paratha pan-fried with ghee.</p></div>
    <div class="dish"><div class="dish-line"><span>Cheese Naan</span><span class="leader"></span><span class="price">$8</span></div><p class="dish-desc">Stuffed with molten cheese, baked in the tandoor.</p></div>
    <div class="dish"><div class="dish-line"><span>Cheese Garlic Naan</span><span class="leader"></span><span class="price">$8.50</span></div><p class="dish-desc">Naan layered with garlic &amp; cheese — indulgent &amp; aromatic.</p></div>
  </section>
  <section class="menu-section col-four" style="left:812px;top:268px;width:215px">
    <h2 class="section-banner">Sides</h2>
    <div class="dish" style="margin-bottom:10px"><div class="dish-line"><span>Cucumber Raita</span><span class="leader"></span><span class="price">$6</span></div><p class="dish-desc">Cool yogurt with cucumber, cumin &amp; mint.</p></div>
    <div class="dish" style="margin-bottom:10px"><div class="dish-line"><span>Roasted Papadum</span><span class="leader"></span><span class="price">$4(4 pcs)</span></div><p class="dish-desc">Crispy lentil wafers roasted for a healthy crunch.</p></div>
    <div class="dish" style="margin-bottom:10px"><div class="dish-line"><span>Masala Papad</span><span class="leader"></span><span class="price">$8(2 pcs)</span></div><p class="dish-desc">Papad topped with spiced onions, tomatoes &amp; herbs.</p></div>
    <div class="dish" style="margin-bottom:10px"><div class="dish-line"><span>Onion Salad</span><span class="leader"></span><span class="price">$6</span></div><p class="dish-desc">Fresh onion rings tossed with lime &amp; masala.</p></div>
    <div class="dish" style="margin-bottom:10px"><div class="dish-line"><span>Garden Salad</span><span class="leader"></span><span class="price">$8</span></div><p class="dish-desc">Seasonal greens dressed with lemon &amp; cumin.</p></div>
    <div class="dish"><div class="dish-line" style="display:block">Mango Chutney / Mint Chutney /</div><div class="dish-line"><span>Mixed Pickle</span><span class="leader"></span><span class="price">$4</span></div><p class="dish-desc" style="margin-top:4px">House-made condiments to complement your meal.</p></div>
  </section>
  <section class="menu-section col-four" style="left:812px;top:511px;width:215px">
    <h2 class="section-banner">Desserts</h2>
    <div class="dish"><div class="dish-line"><span>Kunafa Nest Gulab Jamun with Rabri</span><span class="leader"></span><span class="price">$20</span></div><p class="dish-desc">Golden kunafa nest cradling soft gulab jamun, draped in creamy rabri &amp; pistachios.</p></div>
    <div class="dish"><div class="dish-line"><span>Mango Mousse Delight</span><span class="leader"></span><span class="price">$20</span></div><p class="dish-desc" style="max-width:190px">Alphonso mango mousse layered with coconut crumble &amp; fresh mint.</p></div>
    <div class="dish"><div class="dish-line"><span>Kulfi Falooda Trio</span><span class="leader"></span><span class="price">$20</span></div><p class="dish-desc">Traditional kulfi in pistachio, rose &amp; saffron, served with silky falooda.</p></div>
  </section>

  <div class="brand-block">
    <div class="brand-rule"></div>
    <div class="brand-name">Tara’s Kitchen</div>
  </div>
</div>
</body>
</html>
```